Business Cards and stationery for Land (Real Estate) Development Group
Torvik Group, Land Development and Consulting
Business Cards and stationery  for Land (Real Estate) Development Group - Real Estate
Creative Brief
Professional
Marcus Pellowe
418 West Orchard Ave, Suite 312 Brenham, TX 77561
marcusp@torvikgroup.example
I would like to see designs consisting of either double sided standard sized Business Card [3.5" x 2"] or double sided rounded corner business card 3.35 x 2.2 Let's see if the words "we bring land to life" can be added somewhere on the card - or maybe on the back Also, please provide layouts for stationary as well If the logo, or a portion of the logo, can be placed on the back of the card along with the slogan that would be great.
We bring land to life.
Zentro Zentro
Ok. Can u give some star rating please.
marcusp marcusp
Please feel free to use the "D" logo separately from the text "Torvik Group" if a necessary for a design. Also, separate the tagline if you as the designer feel like it should be larger, etc. Also, please let me see options of business cards with rounded corners as well. Thanks.

```html
<!DOCTYPE html>
<html lang="en">
<head>
<meta charset="utf-8">
<title>Torvik Group – Business Card</title>
<link rel="stylesheet" href="https://fonts.googleapis.com/css2?family=Montserrat:wght@600;700&family=Open+Sans:wght@400;600&display=swap">
<style>
  :root {
    --page-bg: #e6e7e9;
    --card-bg: #ffffff;
    --brand-green: #17773f;
    --brand-green-soft: #a9cdb6;
    --brand-blue: #1f5fa8;
    --ink: #2f3a44;
    --ink-soft: #6a747d;
  }
  * { box-sizing: border-box; margin: 0; padding: 0; }
  html, body {
    width: 1200px; height: 883px; overflow: hidden;
    background: var(--page-bg);
    font-family: "Open Sans", Arial, sans-serif;
    color: var(--ink);
  }
  .stage {
    width: 1200px; height: 883px;
    display: flex; align-items: center; justify-content: center; gap: 60px;
  }
  .card {
    position: relative;
    width: 500px; height: 328px;
    background: var(--card-bg);
    border-radius: 26px;
    overflow: hidden;
    box-shadow: 0 10px 26px rgba(0,0,0,0.12);
  }
  .brand { display: flex; flex-direction: column; align-items: flex-start; }
  .brand-row { display: flex; align-items: center; gap: 8px; }
  .brand-mark { width: 20px; height: 20px; background: var(--brand-green); }
  .brand-name {
    font-family: "Montserrat", Arial, sans-serif;
    font-weight: 700; color: var(--brand-blue);
    letter-spacing: 1.5px; text-transform: uppercase;
    line-height: 1;
  }
  .brand-tagline {
    font-size: 9px; color: var(--brand-green); margin-top: 5px;
    letter-spacing: 0.3px;
  }

  /* Front */
  .card-front .brand { position: absolute; top: 52px; right: 52px; }
  .card-front .brand-name { font-size: 22px; }
  .identity {
    position: absolute; left: 0; top: 84px;
    padding-left: 24px; border-left: 7px solid var(--brand-blue);
  }
  .identity-name {
    font-family: "Montserrat", Arial, sans-serif;
    font-size: 12px; font-weight: 600; text-transform: uppercase; letter-spacing: 0.6px;
  }
  .identity-role { font-size: 10px; color: var(--ink-soft); margin-top: 2px; }
  .contacts {
    position: absolute; left: 32px; top: 142px;
    list-style: none; font-size: 9px; color: var(--ink-soft);
  }
  .contacts li { display: flex; align-items: center; gap: 7px; height: 17px; }
  .contacts svg { width: 9px; height: 9px; fill: var(--ink); }
  .address {
    position: absolute; right: 40px; top: 160px;
    font-size: 9.5px; line-height: 1.45; text-align: right; color: var(--ink-soft);
  }
  .band { position: absolute; left: 0; bottom: 0; width: 500px; height: 130px; }

  /* Back */
  .card-back { display: flex; align-items: center; justify-content: center; }
  .card-back .brand-name { font-size: 28px; }
  .card-back .brand-mark { width: 26px; height: 26px; }
  .card-back .brand-tagline { font-size: 10.5px; }
</style>
</head>
<body>
<main class="stage">

  <section class="card card-front" aria-label="Business card front">
    <div class="brand">
      <div class="brand-row">
        <span class="brand-mark"></span>
        <span class="brand-name">Torvik Group</span>
      </div>
      <span class="brand-tagline">We bring land to life.</span>
    </div>

    <div class="identity">
      <p class="identity-name">Elian Marsh</p>
      <p class="identity-role">Managing Director</p>
    </div>

    <ul class="contacts">
      <li><svg viewBox="0 0 10 10"><path d="M2 0h2l1 3-1.5 1a6 6 0 0 0 2.5 2.5L7 5l3 1v2a2 2 0 0 1-2 2A8 8 0 0 1 0 2a2 2 0 0 1 2-2z"/></svg>555 014 2278</li>
      <li><svg viewBox="0 0 10 10"><rect x="2" y="0" width="6" height="10" rx="1"/></svg>555 014 2279</li>
      <li><svg viewBox="0 0 10 10"><rect x="0" y="3" width="10" height="5" rx="1"/><rect x="2" y="0" width="6" height="3"/></svg>555 014 2280</li>
      <li><svg viewBox="0 0 10 10"><path d="M0 2h10v6H0z"/></svg>mail@torvikgroup.example</li>
      <li><svg viewBox="0 0 10 10"><circle cx="5" cy="5" r="5"/></svg>www.torvikgroup.example</li>
    </ul>

    <p class="address">27 Cedar Bend Blvd,<br>Hollow Creek Road, Millbrook</p>

    <svg class="band" viewBox="0 0 500 130" preserveAspectRatio="none" aria-hidden="true">
      <path d="M0 92 C160 62 340 40 500 30 L500 36 C340 46 160 68 0 98 Z" fill="var(--brand-green-soft)"/>
      <path d="M0 98 C160 68 340 46 500 36 L500 112 C340 114 160 118 0 124 Z" fill="var(--brand-green)"/>
    </svg>
  </section>

  <section class="card card-back" aria-label="Business card back">
    <div class="brand">
      <div class="brand-row">
        <span class="brand-mark"></span>
        <span class="brand-name">Torvik Group</span>
      </div>
      <span class="brand-tagline">We bring land to life.</span>
    </div>
  </section>

</main>
</body>
</html>
```